Elegant Black Candle Label Design!

I need a 2.375" tall by 3.0" wide candle label design. I'm looking for simple and elegant. Black label with silver leaf border and lettering. Label needs to have the following information on it: Fern Hollow Candle Co. as the company name, scent name in the middle and in smaller font, it needs to say Made in USA, All Natural, 8oz. Attached photos are for inspiration.

Target Market(s)

People looking for high end, all natural candle fragrances

Industry/Entity Type

Candle-Spa

Colors

Designer to choose only greyscale colors for use in the design.

Requirements
Must have
• Company Name, Scent (ability to change scent names), All Natural, Made in USA, 8oz
Nice to have
• Black background, silver leaf border and silver leaf font. Elegant fonts maybe slightly cursive

```html
<!DOCTYPE html>
<html lang="en">
<head>
<meta charset="utf-8">
<title>Fern Hollow Candle Co. — Label</title>
<link rel="stylesheet" href="https://fonts.googleapis.com/css2?family=Allura&family=Cormorant+Garamond:ital,wght@0,500;1,500&display=swap">
<style>
  :root {
    --backdrop: #f6f5f4;
    --label-black: #111111;
    --label-edge: #1e1e1e;
    --silver: #dcdcdc;
    --silver-bright: #f0f0f0;
    --silver-mid: #a8a8a8;
    --silver-dim: rgba(200, 200, 200, 0.0);
  }
  html, body {
    margin: 0;
    padding: 0;
    width: 1200px;
    height: 1199px;
    overflow: hidden;
    background: var(--backdrop);
  }
  .label {
    position: absolute;
    left: 100px;
    top: 203px;
    width: 1000px;
    height: 792px;
    background: radial-gradient(ellipse at 50% 45%, var(--label-edge) 0%, var(--label-black) 70%);
    box-shadow: 0 2px 10px rgba(0, 0, 0, 0.18);
    overflow: hidden;
  }
  .label__frame {
    position: absolute;
    inset: 22px;
    border: 2px solid var(--silver-mid);
    pointer-events: none;
  }
  .botanical {
    position: absolute;
    border-radius: 46% 54% 50% 50% / 55% 45% 55% 45%;
    background:
      radial-gradient(ellipse at 40% 45%, var(--silver-bright) 0%, var(--silver-mid) 38%, rgba(150,150,150,0.35) 62%, var(--silver-dim) 80%);
  }
  .botanical--top-left { left: -70px; top: -70px; width: 300px; height: 210px; transform: rotate(-12deg); }
  .botanical--top-center { left: 390px; top: -55px; width: 190px; height: 100px; opacity: 0.7; }
  .botanical--top-right { right: -70px; top: -60px; width: 260px; height: 300px; transform: rotate(18deg); }
  .botanical--bottom-left { left: -60px; bottom: -80px; width: 420px; height: 250px; transform: rotate(6deg); }
  .botanical--bottom-center { left: 380px; bottom: -70px; width: 230px; height: 140px; opacity: 0.85; }
  .botanical--bottom-right { right: -70px; bottom: -80px; width: 360px; height: 280px; transform: rotate(-10deg); }
  .brand {
    position: absolute;
    left: 0;
    right: 0;
    top: 150px;
    text-align: center;
    color: var(--silver);
  }
  .brand__name {
    margin: 0;
    font-family: "Allura", cursive;
    font-weight: 400;
    font-size: 118px;
    line-height: 1;
  }
  .brand__descriptor {
    margin: 4px 0 0;
    font-family: "Cormorant Garamond", serif;
    font-weight: 500;
    font-size: 34px;
    letter-spacing: 0.2em;
    padding-left: 0.2em;
  }
  .scent {
    position: absolute;
    left: 0;
    right: 0;
    top: 352px;
    margin: 0;
    text-align: center;
    font-family: "Cormorant Garamond", serif;
    font-style: italic;
    font-weight: 500;
    font-size: 42px;
    color: var(--silver-bright);
    letter-spacing: 0.03em;
  }
  .details {
    position: absolute;
    left: 0;
    right: 0;
    top: 432px;
    text-align: center;
    font-family: "Cormorant Garamond", serif;
    font-weight: 500;
    font-size: 30px;
    color: var(--silver);
    font-variant: small-caps;
    letter-spacing: 0.04em;
  }
  .details p { margin: 0 0 20px; }
  .details__dot {
    display: inline-block;
    width: 7px;
    height: 7px;
    border-radius: 50%;
    background: var(--silver);
    vertical-align: middle;
    margin: 0 16px;
  }
</style>
</head>
<body>
  <main class="label">
    <div class="botanical botanical--top-left" role="img" aria-label="Silver leaf botanical sprigs with small flowers"></div>
    <div class="botanical botanical--top-center" role="img" aria-label="Silver leaf botanical sprig"></div>
    <div class="botanical botanical--top-right" role="img" aria-label="Silver leaf botanical sprigs with small flowers"></div>
    <div class="botanical botanical--bottom-left" role="img" aria-label="Silver leaf cluster of small flowers and leaves"></div>
    <div class="botanical botanical--bottom-center" role="img" aria-label="Silver leaf sprig of small flowers"></div>
    <div class="botanical botanical--bottom-right" role="img" aria-label="Silver leaf cluster of small flowers and leaves"></div>
    <div class="label__frame"></div>

    <header class="brand">
      <h1 class="brand__name">Fern Hollow</h1>
      <p class="brand__descriptor">CANDLE CO.</p>
    </header>

    <p class="scent">Cedar &amp; Sage</p>

    <section class="details">
      <p>8oz<span class="details__dot"></span>All Natural</p>
      <p>Made in USA</p>
    </section>
  </main>
</body>
</html>
```